Logo & Visitenkarte für Tischwinkel
Zielgruppe
Die Jausenstation mit Hausmannskost
Aufgabenstellung
Telefonnummer 0463 517064
E-Mail tischwinkel@postfeld.de
Und den Firmennamen

```html
<!DOCTYPE html>
<html lang="de">
<head>
<meta charset="utf-8">
<title>Tischwinkel – Visitenkarte</title>
<link rel="stylesheet" href="https://fonts.googleapis.com/css2?family=Oswald:wght@500;600&display=swap">
<style>
  :root {
    --stage: #8c7464;
    --orange-deep: #f98a0c;
    --orange-light: #fbab56;
    --cream: #ede8cb;
    --cream-pattern: #f3efd6;
    --brown: #5a3514;
    --white: #ffffff;
    --pill: #f7941d;
  }
  * { margin: 0; padding: 0; box-sizing: border-box; }
  html, body {
    width: 1102px;
    height: 1200px;
    overflow: hidden;
  }
  body {
    background: var(--stage);
    position: relative;
    font-family: "Oswald", sans-serif;
  }
  .card {
    position: absolute;
    left: 211px;
    width: 687px;
    height: 395px;
    overflow: hidden;
  }
  .card--front {
    top: 116px;
    background: linear-gradient(90deg, var(--orange-deep) 0%, var(--orange-light) 100%);
  }
  .card--back {
    top: 554px;
    background: var(--cream);
  }
  .faint-name {
    position: absolute;
    font-weight: 600;
    color: #000;
    opacity: 0.05;
    white-space: nowrap;
    line-height: 1;
  }
  .faint-name--top { left: -40px; top: -40px; font-size: 150px; }
  .faint-name--bottom { left: 300px; top: 250px; font-size: 170px; }
  .brand {
    position: absolute;
    display: flex;
    align-items: center;
    gap: 14px;
    font-weight: 600;
    white-space: nowrap;
    line-height: 1;
  }
  .brand__dot {
    width: 22px;
    height: 22px;
    border-radius: 50%;
  }
  .card--front .brand {
    left: 50%;
    top: 168px;
    transform: translate(-50%, -50%);
    font-size: 72px;
    color: var(--white);
  }
  .card--front .brand__dot { background: var(--white); }
  .food-pattern {
    position: absolute;
    inset: 0;
    background: linear-gradient(135deg, var(--cream) 0%, var(--cream-pattern) 50%, var(--cream) 100%);
  }
  .card--back .brand {
    left: 320px;
    top: 162px;
    transform: translate(-50%, -50%) rotate(-14deg);
    font-size: 64px;
    color: var(--brown);
  }
  .card--back .brand__dot { background: var(--pill); }
  .phone-pill {
    position: absolute;
    left: 478px;
    top: 228px;
    transform: translate(-50%, -50%) rotate(-14deg);
    padding: 5px 22px;
    background: var(--pill);
    border-radius: 24px;
    color: var(--brown);
    font-size: 26px;
    font-weight: 500;
    letter-spacing: 1px;
    line-height: 1.2;
    white-space: nowrap;
  }
</style>
</head>
<body>
  <section class="card card--front" aria-label="Vorderseite">
    <span class="faint-name faint-name--top" aria-hidden="true">Tischwinkel</span>
    <span class="faint-name faint-name--bottom" aria-hidden="true">Tischwinkel</span>
    <div class="brand">
      <span class="brand__dot"></span>
      <span class="brand__name">Tischwinkel</span>
    </div>
  </section>

  <section class="card card--back" aria-label="Rückseite">
    <div class="food-pattern" role="img" aria-label="Hellcremefarbenes Muster aus gezeichneten Burgern, Sandwiches, Pizza und Pommes"></div>
    <div class="brand">
      <span class="brand__dot"></span>
      <span class="brand__name">Tischwinkel</span>
    </div>
    <div class="phone-pill">0463517064</div>
  </section>
</body>
</html>
```